Product Setup Instructional Infographic/flyer

Converting product instructions into an infographic. Would prefer that the instructions fit on a 4x6 card, front and back, but a slightly larger size is acceptable as well.

Logo Text

Ridgeline Cask (Rebranding just as Ridgeline Cask, instead of Ridgeline Cask Barrels)

Font styles to use
Decorative

Colors

Designer to choose colors to be used in the design.

Requirements
Must have
• NA
Nice to have
• NA
Should not have
• NA

```html
<!DOCTYPE html>
<html lang="en">
<head>
<meta charset="utf-8">
<title>Barrel Curing Guide Card</title>
<link href="https://fonts.googleapis.com/css2?family=Pinyon+Script&family=Didact+Gothic&family=Pathway+Gothic+One&family=Oswald:wght@400;600&display=swap" rel="stylesheet">
<style>
:root{
  --bg:#ece8ea;
  --paper:#ffffff;
  --gold:#fcc400;
  --gold-deep:#e0a800;
  --bark:#7a6650;
  --ink:#2a2520;
  --rule:#b9a993;
  --photo-sky:#aab6c6;
  --photo-green:#5d7a3e;
  --photo-wood:#5a4230;
}
*{margin:0;padding:0;box-sizing:border-box}
html,body{width:1200px;height:973px;overflow:hidden;background:var(--bg)}
.card{position:absolute;top:88px;width:482px;height:722px;background:var(--paper);overflow:hidden;box-shadow:0 4px 14px rgba(0,0,0,.18)}
.card--front{left:103px}
.card--back{left:618px}

/* front */
.front-photo{position:absolute;left:0;top:0;width:482px;height:520px;
  background:linear-gradient(180deg,var(--photo-sky) 0%,#c8cfd6 22%,var(--photo-green) 40%,var(--photo-wood) 58%,#3b2a1e 100%)}
.front-wave{position:absolute;left:0;top:0}
.front-title{position:absolute;left:0;right:0;top:538px;text-align:center;
  font-family:"Pinyon Script",cursive;font-weight:400;font-size:64px;color:var(--bark);line-height:1}
.front-sub{position:absolute;left:0;right:0;top:614px;text-align:center;
  font-family:"Didact Gothic",sans-serif;font-size:30px;line-height:31px;color:var(--bark)}
.front-bar{position:absolute;left:219px;top:686px;width:44px;height:3px;background:var(--gold)}

/* back */
.back-header{position:absolute;left:0;top:0}
.back-intro{position:absolute;left:16px;right:16px;top:30px;text-align:center;
  font-family:"Pathway Gothic One",sans-serif;font-size:14.5px;line-height:18px;color:#fff}
.back-intro p+p{margin-top:6px}
.step{position:absolute;left:0;right:0}
.step-tag{position:absolute;left:16px;top:0;width:70px;height:27px;background:var(--gold);
  clip-path:polygon(0 0,88% 0,100% 50%,88% 100%,0 100%);
  font-family:"Oswald",sans-serif;font-weight:600;font-size:15px;line-height:27px;
  padding-left:6px;color:var(--bark);letter-spacing:.3px}
.step-tag::after{content:"";position:absolute;left:0;bottom:0;width:8px;height:4px;background:var(--gold-deep)}
.step-text{position:absolute;left:99px;right:14px;top:2px;
  font-family:"Pathway Gothic One",sans-serif;font-size:14px;line-height:16px;color:var(--ink)}
.rule{position:absolute;left:99px;right:14px;height:1px;background:var(--rule)}
.tip{position:absolute;left:19px;top:616px;width:443px;height:106px;background:var(--gold);padding:16px 26px 0}
.tip-head{display:flex;align-items:center;gap:8px;font-family:"Oswald",sans-serif;font-weight:400;font-size:16px;color:var(--ink);text-transform:uppercase}
.tip-head::before,.tip-head::after{content:"";flex:1;height:1px;background:var(--ink)}
.tip-text{margin-top:8px;text-align:center;font-family:"Pathway Gothic One",sans-serif;font-size:14px;line-height:16px;color:var(--ink)}
</style>
</head>
<body>

<section class="card card--front">
  <div class="front-photo" role="img" aria-label="Photo of two weathered oak barrels standing outdoors in front of a vineyard and misty hills"></div>
  <svg class="front-wave" width="482" height="722" viewBox="0 0 482 722" aria-hidden="true">
    <path d="M0 430 C40 478 100 502 170 498 C262 490 340 362 482 322 L482 722 L0 722 Z" fill="#fcc400"/>
    <path d="M0 458 C50 500 112 514 182 508 C272 498 352 384 482 343 L482 722 L0 722 Z" fill="#7a6650"/>
    <path d="M0 463 C50 505 112 519 182 513 C272 503 352 392 482 352 L482 722 L0 722 Z" fill="#fcc400"/>
    <path d="M0 478 C60 510 130 522 200 516 C290 506 380 450 482 440 L482 722 L0 722 Z" fill="#ffffff"/>
  </svg>
  <h1 class="front-title">A Step By Step</h1>
  <p class="front-sub">Guide On How To Cure<br>Your Oak Barrel</p>
  <div class="front-bar"></div>
</section>

<section class="card card--back">
  <svg class="back-header" width="482" height="160" viewBox="0 0 482 160" role="img" aria-label="Dim cellar photo of stacked oak barrels">
    <defs>
      <linearGradient id="cellar" x1="0" y1="0" x2="1" y2="1">
        <stop offset="0" stop-color="#3a2616"/>
        <stop offset=".5" stop-color="#22140b"/>
        <stop offset="1" stop-color="#4b3020"/>
      </linearGradient>
    </defs>
    <path d="M0 0 H482 V118 C380 160 300 160 240 152 C150 140 60 120 0 128 Z" fill="url(#cellar)"/>
  </svg>
  <div class="back-intro">
    <p>First, we would like to thank you for choosing Ridgeline Cask Barrels for your home spirit and wine-aging needs. We know you are very excited to use it and so are we.</p>
    <p>However, your barrel is NOT ready yet for use. You need to cure it first to get rid of the wood debris and make it watertight. Do not fret, we laid out an easy to follow step by step guide on how to ready your barrel for spirit and wine-aging.</p>
  </div>

  <div class="step" style="top:176px"><span class="step-tag">STEP 1</span><p class="step-text">Rinse and soak the spigot (wooden faucet) and the plug (or bung) in water for about half an hour.</p></div>
  <div class="rule" style="top:214px"></div>
  <div class="step" style="top:226px"><span class="step-tag">STEP 2</span><p class="step-text">While waiting, fill the barrel with water until it is half-full. Use your thumb to plug the holes, give it a good shake to get rid of wood chips and debris that might be trapped inside. Let the water out. You may repeat this process three to five times until you satisfied the barrel is thoroughly clean.</p></div>
  <div class="rule" style="top:301px"></div>
  <div class="step" style="top:314px"><span class="step-tag">STEP 3</span><p class="step-text">Plug the barrel with the spigot. You may tighten it securely with your hand. We advise not to use a hammer as it may crack the wood.</p></div>
  <div class="rule" style="top:358px"></div>
  <div class="step" style="top:367px"><span class="step-tag">STEP 4</span><p class="step-text">Place the barrel in a sink, tub, or any place that is OK to get wet.</p></div>
  <div class="rule" style="top:394px"></div>
  <div class="step" style="top:406px"><span class="step-tag">STEP 5</span><p class="step-text">Using a funnel, fill the barrel with hot water until it is full. Leave the top hole open. Your barrel might leak, and that’s OK. It is not watertight yet and this process will make the wood expand to seal the gaps.</p></div>
  <div class="rule" style="top:468px"></div>
  <div class="step" style="top:482px"><span class="step-tag">STEP 6</span><p class="step-text">Leave the barrel this way until no more leakages can be seen. This means the wood has expanded and the gaps are sealed. This can take from 30 minutes to an entire week, depending on the size of the barrel.</p></div>
  <div class="rule" style="top:538px"></div>
  <div class="step" style="top:550px"><span class="step-tag">STEP 7</span><p class="step-text">Drain the barrel and let it air dry for no more than four hours. After 4 hours, it is ready to be filled with any spirits or wine of your choice.</p></div>

  <div class="tip">
    <h2 class="tip-head">Additional Tip</h2>
    <p class="tip-text">If you plan on aging different kinds of alcohol using the same barrel, you must cure the barrel again (Step 6) for three to five days. This will allow the barrel to absorb enough water and prevent the next batch of alcohol from being contaminated.</p>
  </div>
</section>

</body>
</html>
```